Need someone to revamp my signboard

I own a Manicure Salon. The current signboard design is very clean in look with black and white to complement my shop design. But my shop is undergoing a major reno and the new design is more feminine, elegant with wooden flooring and white cabinets. VELMORA by Tova & Reed is the name of the shop. Tova and Reed is the holding company. So I would like it to be incorporated in the signage too.
The new colour should be beige, brown with hint of red to communicate feminine as well as elegant feel.

Industry/Entity Type

Shop

```html
<!DOCTYPE html>
<html lang="en">
<head>
<meta charset="utf-8">
<title>VELMORA by Tova &amp; Reed — Signboard</title>
<link rel="stylesheet" href="https://fonts.googleapis.com/css2?family=Josefin+Sans:wght@200;300&display=swap">
<style>
  :root {
    --cream: #fdf0e0;
    --brown: #6e3a1c;
    --brown-soft: rgba(110, 58, 28, 0.42);
    --brown-mid: rgba(110, 58, 28, 0.18);
    --brown-faint: rgba(110, 58, 28, 0.07);
  }
  html, body {
    margin: 0;
    padding: 0;
    overflow: hidden;
    background: var(--cream);
  }
  .signboard {
    position: relative;
    width: 1200px;
    height: 400px;
    overflow: hidden;
    background: var(--cream);
  }
  .background-flourish {
    position: absolute;
    inset: 0;
    background:
      radial-gradient(ellipse 420px 140px at 150px 200px, var(--brown-faint), transparent 70%),
      radial-gradient(ellipse 420px 140px at 1050px 200px, var(--brown-faint), transparent 70%),
      radial-gradient(ellipse 500px 120px at 600px 40px, var(--brown-faint), transparent 70%),
      radial-gradient(ellipse 500px 120px at 600px 360px, var(--brown-faint), transparent 70%);
  }
  .ornament {
    position: absolute;
    background: radial-gradient(ellipse at center, var(--brown-soft) 0%, var(--brown-mid) 45%, transparent 72%);
  }
  .ornament--top {
    left: 300px;
    top: 10px;
    width: 600px;
    height: 110px;
  }
  .ornament--bottom {
    left: 290px;
    top: 270px;
    width: 620px;
    height: 120px;
  }
  .shop-name {
    position: absolute;
    left: 0;
    top: 140px;
    width: 1200px;
    margin: 0;
    font-family: "Josefin Sans", sans-serif;
    font-weight: 200;
    font-size: 100px;
    line-height: 1;
    letter-spacing: 6px;
    text-align: center;
    color: var(--brown);
  }
  .subline {
    position: absolute;
    left: 0;
    top: 236px;
    width: 1200px;
    margin: 0;
    font-family: "Josefin Sans", sans-serif;
    font-weight: 300;
    font-size: 19px;
    letter-spacing: 4px;
    text-transform: uppercase;
    text-align: center;
    color: var(--brown);
    white-space: nowrap;
  }
  .subline__dot {
    display: inline-block;
    width: 5px;
    height: 5px;
    margin: 0 18px 4px;
    border-radius: 50%;
    background: var(--brown);
    vertical-align: middle;
  }
</style>
</head>
<body>
  <main class="signboard">
    <div class="background-flourish" role="img" aria-label="Faint scrolling flourish pattern across the background"></div>
    <div class="ornament ornament--top" role="img" aria-label="Brown ornamental scroll flourish above the shop name"></div>
    <h1 class="shop-name">VELMORA</h1>
    <p class="subline">Grace in every detail<span class="subline__dot"></span>by Tova &amp; Reed</p>
    <div class="ornament ornament--bottom" role="img" aria-label="Brown ornamental scroll flourish below the shop name"></div>
  </main>
</body>
</html>
```